HiItsJonBrell.com needs a modern, eye-catching business card design

My name is Jon Brell and I own a video training (software development industry) website. I need a business card design that is eye catching for when I travel to conferences or do seminars. I would prefer something simple but bold. Something along the lines of this: https://pixvaultstatic.example/gallery_img/530172/44018/44018_9917302_530172_image.jpg

Note that I do not have a specific logo, but I do have an caricature I use on my site of myself. I've not attached it because I'm not really a fan of having it on my business cards. I would prefer lettering instead of an image. You can go to my website (https://hiitsjonbrell.com) for inspiration.

I want to add the following information on my card (the order of these, their size, and their casing is up to you):

Jon Brell
jon@HiItsJonBrell.com
@HiItsJonBrell
HiItsJonBrell.com
vidsharehub.example/HiItsJonBrell

I would also like to have somewhere on the card a small ad that says "Get a free course at https://HiItsJonBrell.com/FreeCourse". Feel free to play with that wording or layout if you need. I would prefer this text to be at the bottom of the card and subtle. Some small eye-catching thing might be ok but nothing huge or garish.

I plan on printing this card at pressquill.example (https://www.pressquill.example/us/design-guidelines/business-cards.html). I would like it to be the standard size (3.66" x 2.16"). I would prefer rounded corners and horizontal orientation. This is a two-side design. I would prefer the side with all of the information be primarily white but I like color text (again, flexible on that). On the front side, I like simple. Maybe just HiItsJonBrell.com (casing on that is up to you - whatever looks and reads the best - that goes for all of the casing). As for font choices, I prefer a modern, clean font. For example, Open Sans Light can be a nice option.

Website Info (might be helpful for the card):
Color Palette

Darkest blue - #263246
Alternate blue - #2F4E6A
Light blue - #2A98C3
Orange - #FF6201
White - #FFFFFF

Font for Jon Brell Logo

Jellyka Estryas Handwriting
http://www.typecrate.example/jellyka_estryas_handwriting.font

Fonts for Site Content and VidShare Thumbnails

Lovelo (bold title font)
http://www.glyphmill.example/lovelo-font/

Open Sans (body font)
http://www.letterbarn.example/fonts/open-sans

Industry/Entity Type

Software Development

Contact Information for Business Card

Jon Brell
jon@HiItsJonBrell.com
@HiItsJonBrell
HiItsJonBrell.com
vidsharehub.example/HiItsJonBrell

Get a free course at https://HiItsJonBrell.com/FreeCourse

Colors

Designer to choose colors to be used in the design.

Requirements
Nice to have
• Modern color - maybe primarily a color on the front and then that color as an accent on the back.
Should not have
• Lots of colors - I LOVE color but do not want a rainbow of colors on the card.

```html
<!DOCTYPE html>
<html lang="en">
<head>
<meta charset="utf-8">
<title>Jon Brell – Business Card</title>
<link href="https://fonts.googleapis.com/css2?family=Open+Sans:wght@300;600;700&display=swap" rel="stylesheet">
<style>
  :root {
    --darkest-blue: #263246;
    --card-blue: #2e3b55;
    --light-blue: #2A98C3;
    --orange: #FF6201;
    --orange-soft: #ff7a26;
    --white: #FFFFFF;
    --stage: #0c0f16;
  }
  * { margin: 0; padding: 0; box-sizing: border-box; }
  html, body { width: 1200px; height: 1200px; overflow: hidden; background: var(--stage); }
  .canvas { position: relative; width: 1200px; height: 1200px; font-family: "Open Sans", sans-serif; }

  .card { position: absolute; left: 140px; width: 920px; height: 542px; overflow: hidden; }

  .card-front { top: 50px; background: radial-gradient(ellipse at 50% 45%, var(--card-blue) 0%, var(--darkest-blue) 75%); }
  .corner-accent { position: absolute; inset: 0; width: 100%; height: 100%; }

  .wordmark { position: absolute; left: 0; right: 0; top: 214px; text-align: center;
    color: var(--white); font-weight: 300; font-size: 92px; letter-spacing: 1px; line-height: 1; }
  .site-tag { position: absolute; left: 246px; top: 337px; height: 37px; padding: 0 13px;
    background: var(--light-blue); color: var(--white); font-weight: 700; font-size: 27px;
    line-height: 37px; white-space: nowrap; }

  .card-back { top: 608px; background: var(--white); }
  .contact { position: absolute; left: 0; right: 0; top: 118px; text-align: center; }
  .contact-name { color: var(--orange); font-weight: 700; font-size: 46px; line-height: 54px; letter-spacing: 1px; }
  .contact-line { display: flex; align-items: center; justify-content: center; gap: 8px;
    color: var(--darkest-blue); font-weight: 600; font-size: 31px; line-height: 37px; letter-spacing: 0.5px; }
  .contact-line svg { width: 26px; height: 26px; flex: none; }
  .network-name { font-weight: 600; font-size: 20px; color: var(--darkest-blue); }

  .footer-rule { position: absolute; left: 0; right: 0; top: 448px; height: 8px; background: var(--darkest-blue); }
  .promo { position: absolute; left: 0; right: 0; top: 456px; bottom: 0; background: var(--orange);
    color: var(--white); text-align: center; font-weight: 700; font-size: 27px; line-height: 28px;
    padding-top: 14px; }
</style>
</head>
<body>
<div class="canvas">

  <section class="card card-front">
    <svg class="corner-accent" viewBox="0 0 920 542" preserveAspectRatio="none" role="img" aria-label="Bold orange diagonal stripe decoration in two corners">
      <defs>
        <linearGradient id="accent-fill" x1="0" y1="0" x2="1" y2="1">
          <stop offset="0" stop-color="#FF6201"/>
          <stop offset="1" stop-color="#ff7a26"/>
        </linearGradient>
      </defs>
      <polygon fill="url(#accent-fill)" points="0,0 290,0 0,290"/>
      <polygon fill="url(#accent-fill)" points="920,542 630,542 920,252"/>
    </svg>
    <h1 class="wordmark">Jon Brell</h1>
    <div class="site-tag">HIITSJONBRELL.COM</div>
  </section>

  <section class="card card-back">
    <div class="contact">
      <h2 class="contact-name">JON BRELL</h2>
      <p class="contact-line">
        <svg viewBox="0 0 24 24" aria-hidden="true"><circle cx="12" cy="12" r="10" fill="none" stroke="#263246" stroke-width="2.4"/><path d="M2 12h20M12 2c3 3 3 17 0 20M12 2c-3 3-3 17 0 20" fill="none" stroke="#263246" stroke-width="2"/></svg>
        HiItsJonBrell.com
      </p>
      <p class="contact-line">
        <svg viewBox="0 0 28 24" aria-hidden="true" style="width:32px"><rect x="2" y="4" width="24" height="16" fill="none" stroke="#263246" stroke-width="2"/><path d="M2 4l12 10 12-10M2 20l9-8M26 20l-9-8" fill="none" stroke="#263246" stroke-width="2"/></svg>
        jon@HiItsJonBrell.com
      </p>
      <p class="contact-line">
        <svg viewBox="0 0 24 24" aria-hidden="true"><circle cx="12" cy="12" r="10" fill="none" stroke="#263246" stroke-width="2"/><circle cx="15.5" cy="7.5" r="2" fill="#263246"/><circle cx="15.5" cy="16.5" r="2" fill="#263246"/><circle cx="8" cy="12" r="2" fill="#263246"/><path d="M15.5 7.5L8 12l7.5 4.5" fill="none" stroke="#263246" stroke-width="1.6"/></svg>
        @HiItsJonBrell
      </p>
      <p class="contact-line">
        <span class="network-name">VidShare</span>
        vidsharehub.example/HiItsJonBrell
      </p>
    </div>
    <div class="footer-rule"></div>
    <div class="promo">
      <p>GET A FREE COURSE AT</p>
      <p>https://HiItsJonBrell.com/FreeCourse</p>
    </div>
  </section>

</div>
</body>
</html>
```